Breast Cancer Stickers

Hi,
i would like a of small design for a breast cancer awareness campaign. please check attached picture this is the size and font i want. these will be stickers. Then i would like a little pink ribbon after each dot. so there will be four design please find below colors, slogans, etc..
1 I PINK I CAN. (Off white Background, Light Pink Font)
Never give up.
2 PINK POWER. (Black Background, Bright Pink Font)
Theres Always hope
3 POSITIVELY PINK. ( Light Pink Background, Off white Font)
Stay Positive
4 TURN UP THE PINK. (Bright Pink Background, Black font)
fight on.
Campaign

```html
<!DOCTYPE html>
<html lang="en">
<head>
<meta charset="UTF-8">
<title>Awareness Sticker Set</title>
<link rel="stylesheet" href="https://fonts.googleapis.com/css2?family=Arimo:wght@700&display=swap">
<style>
  :root {
    --stage: #262527;
    --off-white: #ffffff;
    --light-pink: #f19fba;
    --ink-black: #1c1a1f;
    --bright-pink: #e0007b;
    --sticker-size: 332px;
  }
  html, body {
    margin: 0;
    padding: 0;
    width: 1200px;
    height: 900px;
    overflow: hidden;
    background: var(--stage);
  }
  .sticker-sheet {
    position: relative;
    width: 1200px;
    height: 900px;
  }
  .sticker {
    position: absolute;
    width: var(--sticker-size);
    height: var(--sticker-size);
    box-sizing: border-box;
    padding-left: 49px;
    font-family: "Arimo", Arial, sans-serif;
    font-weight: 700;
  }
  .sticker--never-give-up { left: 257px; top: 106px; background: var(--off-white);   color: var(--light-pink);  padding-top: 90px; }
  .sticker--pink-power    { left: 611px; top: 106px; background: var(--ink-black);   color: var(--bright-pink); padding-top: 80px; }
  .sticker--positively    { left: 257px; top: 461px; background: var(--light-pink);  color: var(--off-white);   padding-top: 99px; }
  .sticker--turn-up       { left: 611px; top: 461px; background: var(--bright-pink); color: var(--ink-black);   padding-top: 63px; }

  .slogan {
    margin: 0;
    font-size: 62px;
    line-height: 55px;
    letter-spacing: 0;
    white-space: nowrap;
  }
  .sticker--positively .slogan {
    font-size: 54px;
    line-height: 48px;
  }
  .tagline {
    margin: 14px 0 0;
    font-size: 23px;
    line-height: 24px;
  }
  .sticker--pink-power .tagline { width: 210px; }

  .accent-dot {
    display: inline-block;
    width: 14px;
    height: 14px;
    margin-left: 8px;
    border-radius: 50%;
    vertical-align: 0.1em;
  }
  .accent-dot--bright { background: var(--bright-pink); }
  .accent-dot--light  { background: var(--light-pink); }
</style>
</head>
<body>
<main class="sticker-sheet">

  <section class="sticker sticker--never-give-up">
    <h2 class="slogan">I pink<br>i can.<span class="accent-dot accent-dot--bright" aria-hidden="true"></span></h2>
    <p class="tagline">Never give up.</p>
  </section>

  <section class="sticker sticker--pink-power">
    <h2 class="slogan">Pink<br>power.<span class="accent-dot accent-dot--light" aria-hidden="true"></span></h2>
    <p class="tagline">There’s always hope.</p>
  </section>

  <section class="sticker sticker--positively">
    <h2 class="slogan">Positively<br>pink.<span class="accent-dot accent-dot--bright" aria-hidden="true"></span></h2>
    <p class="tagline">Stay positive.</p>
  </section>

  <section class="sticker sticker--turn-up">
    <h2 class="slogan">Turn up<br>the<br>pink.<span class="accent-dot accent-dot--light" aria-hidden="true"></span></h2>
    <p class="tagline">Fight on.</p>
  </section>

</main>
</body>
</html>
```